Postcard Design

Brightpath Spine Clinic.

On the Front-
I want to create a fall food and toy drive with a snow man on the front with some Christmas trees and snow. It needs to say something like bring a canned food or toy and receive a free initial exam a 150.00 dollar value. phone number on the front 913-555-0142.

On the back-
A large map of location 27815 Hollin Ave. Overland Park Kansas 66213

Services we offer- Diversified Adjusting, Physiotherapy, ultrasound therapy, electrothearpy, intersegmental traction, decompression thearpy, and more!!

Don't forget about our after hour care. Call the after hour number at 913-555-0187
Updates

How about a picture of BRUNO the Pellway character in GLIMMER the movie on the front right of the card some snow on the ground and a few trees in the distance?

The post card is going to be 5.5"x8.5" not your standard 4x6..

Colors
0455a3
ec2027
f04a50
f68d4d
faa54b
fbc994
fde08a
f59296
85acd3

```html
<!DOCTYPE html>
<html lang="en">
<head>
<meta charset="utf-8">
<title>Brightpath Spine Clinic – Food &amp; Toy Drive Postcard</title>
<link href="https://fonts.googleapis.com/css2?family=Arimo:wght@400;700&display=swap" rel="stylesheet">
<style>
  :root {
    --page: #ffffff;
    --white: #ffffff;
    --red: #ec2027;
    --red-deep: #c8161d;
    --green: #5fae3c;
    --green-light: #a9d68c;
    --snow: #f3f4f6;
    --snow-shade: #d9dde3;
    --ornament: #c9141b;
    --ornament-glow: #f04a50;
    --tree: #2f6b2a;
    --gold: #faa54b;
    --map: #e6e3dc;
    --map-road: #cfc9bd;
  }
  * { margin: 0; padding: 0; box-sizing: border-box; }
  html, body {
    width: 1200px; height: 909px; overflow: hidden;
    background: var(--page);
    font-family: "Arimo", Arial, sans-serif;
  }

  /* ---------- back of card ---------- */
  .card-back {
    position: absolute; left: 290px; top: 32px;
    width: 878px; height: 640px;
    background: linear-gradient(135deg, var(--red) 0%, var(--red-deep) 100%);
    overflow: hidden;
  }
  .services { position: absolute; left: 40px; top: 22px; width: 630px; color: var(--white); }
  .services__title { font-size: 21px; line-height: 1.2; }
  .services__list { margin-top: 14px; font-size: 21px; line-height: 1.28; }
  .tree-art {
    position: absolute; left: 700px; top: 8px; width: 160px; height: 205px;
    background: radial-gradient(ellipse at 50% 60%, var(--tree) 0%, #3f8a35 40%, rgba(47,107,42,0) 72%),
                radial-gradient(circle at 50% 8%, var(--gold) 0%, rgba(250,165,75,0) 14%);
  }
  .after-hours {
    position: absolute; right: 30px; top: 222px;
    color: var(--white); font-weight: 700; font-size: 30px; letter-spacing: 0.5px;
  }
  .map-art {
    position: absolute; left: 650px; top: 274px; width: 200px; height: 250px;
    border-radius: 0 90px 0 0;
    background: linear-gradient(180deg, var(--map) 0%, var(--map-road) 100%);
  }
  .gifts-art {
    position: absolute; left: 650px; top: 524px; width: 228px; height: 26px;
    background: linear-gradient(90deg, var(--gold), var(--red-deep), var(--gold));
  }
  .mail-box {
    position: absolute; left: 690px; top: 556px; width: 150px; height: 74px;
    background: var(--white);
  }

  /* ---------- front of card ---------- */
  .card-front {
    position: absolute; left: 32px; top: 176px;
    width: 900px; height: 630px;
    background: var(--white);
    overflow: hidden;
    box-shadow: 0 4px 14px rgba(0,0,0,0.25);
  }
  .card-front__bg { position: absolute; inset: 0; width: 100%; height: 100%; }
  .snowman-art {
    position: absolute; left: 540px; top: 40px; width: 350px; height: 480px;
    background: radial-gradient(ellipse at 50% 50%, var(--snow) 0%, var(--snow-shade) 48%, rgba(236,32,39,0.22) 64%, rgba(255,255,255,0) 74%);
  }
  .ornament-art {
    position: absolute; left: 20px; top: 486px; width: 230px; height: 110px;
    background: radial-gradient(ellipse at 45% 50%, var(--ornament-glow) 0%, var(--ornament) 38%, rgba(201,20,27,0) 72%);
  }
  .brand {
    position: absolute; left: 56px; top: 58px;
    color: var(--red); font-weight: 700; font-size: 40px; line-height: 1.05;
  }
  .drive { position: absolute; left: 108px; top: 266px; }
  .drive__kicker { color: var(--red); font-weight: 700; font-size: 32px; line-height: 1; }
  .drive__title { color: var(--green); font-weight: 700; font-size: 62px; line-height: 1; margin-top: 2px; letter-spacing: 1px; }
  .offer {
    position: absolute; left: 60px; top: 370px; width: 470px;
    text-align: center; color: var(--red); font-size: 23px; line-height: 1.22;
  }
  .offer__price { font-weight: 700; font-size: 28px; }
  .offer__note { color: var(--green); font-size: 26px; }
  .contact {
    position: absolute; right: 40px; bottom: 38px;
    display: flex; align-items: center; gap: 12px;
    color: var(--white); font-weight: 700; font-size: 40px; letter-spacing: 1px;
  }
  .contact__icon { width: 34px; height: 34px; }
</style>
</head>
<body>
  <section class="card-back">
    <div class="services">
      <p class="services__title">Services we offer</p>
      <p class="services__list">Diversified Adjusting, Physiotherapy, ultrasound therapy, electrothearpy, intersegmental traction, decompression thearpy, and more!!</p>
    </div>
    <div class="tree-art" role="img" aria-label="Decorated Christmas tree with a gold star"></div>
    <p class="after-hours">913-555-0187</p>
    <div class="map-art" role="img" aria-label="Street map showing the clinic location"></div>
    <div class="gifts-art" role="img" aria-label="Wrapped presents under the tree"></div>
    <div class="mail-box"></div>
  </section>

  <main class="card-front">
    <svg class="card-front__bg" viewBox="0 0 900 630" aria-hidden="true">
      <path d="M0 0 H900 V70 C650 95 320 150 0 205 Z" fill="var(--green)"/>
      <path d="M0 205 C320 150 650 95 900 70 V82 C650 108 320 163 0 218 Z" fill="var(--green-light)"/>
      <path d="M0 500 C280 470 600 452 900 462 V630 H0 Z" fill="var(--green)"/>
      <path d="M0 526 C280 500 600 486 900 496 V630 H0 Z" fill="var(--red)"/>
    </svg>

    <div class="snowman-art" role="img" aria-label="Snowman in a striped red and green knit hat and scarf, waving a red mitten"></div>
    <div class="ornament-art" role="img" aria-label="Red Christmas ornaments with pine sprigs and snow"></div>

    <div class="brand">Brightpath Spine<br>Clinic</div>

    <div class="drive">
      <div class="drive__kicker">FOOD &amp; TOY</div>
      <div class="drive__title">DRIVE</div>
    </div>

    <p class="offer">
      Bring a canned food or toy<br>
      and receive a free initial exam<br>
      A <span class="offer__price">$150</span> <span class="offer__note">dollar value</span>
    </p>

    <div class="contact">
      <svg class="contact__icon" viewBox="0 0 40 40" aria-hidden="true">
        <circle cx="20" cy="20" r="17" fill="none" stroke="var(--white)" stroke-width="3"/>
        <path d="M14 11 l4 0 l2 6 l-3 2 c1 3 3 5 6 6 l2 -3 l6 2 l0 4 c-10 1 -18 -7 -17 -17 z" fill="var(--white)"/>
      </svg>
      <span class="contact__phone">913-555-0142</span>
    </div>
  </main>
</body>
</html>
```